Engineering Consultant Business Card

I'm starting a new business as a high-end engineering consultant in a niche field. I've attached the jpg for my logo plus the branding guideline document that I've been following. You can see my business website here: www.tarvikworks.com
I'd like a business card that has the logo on one side, then the other side has (in any order): Tarvik Works, Inc.
Dana Whitlock
President and Chief EMC Engineer
www.tarvikworks.com
dana@tarvikworks.com
Optional: motto "We will solve your EMC problems as early as possible—ideally before they even start."
I'm not planning on including a phone number
Target Market(s)
Businesses, especially makers of electronics hardware
Industry/Entity Type
Electrical engineering
Contact Information for Business Card
Company name, my name, website, email

```html
<!DOCTYPE html>
<html lang="en">
<head>
<meta charset="utf-8">
<title>Tarvik Works, Inc. — Business Card</title>
<link rel="stylesheet" href="https://fonts.googleapis.com/css2?family=Poppins:wght@300;400;500;600;700&display=swap">
<style>
  :root {
    --backdrop: #1d1f20;
    --card: #fbfcfc;
    --brand-blue: #3a73e4;
    --ink: #111111;
    --card-radius: 26px;
  }
  * { box-sizing: border-box; margin: 0; padding: 0; }
  html, body {
    width: 1200px;
    height: 859px;
    overflow: hidden;
    background: var(--backdrop);
    font-family: "Poppins", sans-serif;
  }
  .canvas {
    position: relative;
    width: 1200px;
    height: 859px;
  }
  .card {
    position: absolute;
    left: 300px;
    width: 600px;
    height: 343px;
    background: var(--card);
    border-radius: var(--card-radius);
    box-shadow: 0 14px 40px rgba(0, 0, 0, 0.45);
    overflow: hidden;
  }
  .card--front { top: 62px; }
  .card--back { top: 452px; }

  /* Brand mark: name with a single plain ring */
  .brand-mark {
    display: flex;
    align-items: center;
    gap: 14px;
    color: var(--brand-blue);
    font-weight: 600;
    white-space: nowrap;
  }
  .brand-mark__ring {
    flex: none;
    border: 6px solid var(--brand-blue);
    border-radius: 50%;
  }

  /* Front */
  .card--front .brand-mark {
    position: absolute;
    left: 50%;
    top: 118px;
    transform: translateX(-50%);
    font-size: 38px;
  }
  .card--front .brand-mark__ring { width: 54px; height: 54px; }
  .motto {
    position: absolute;
    left: 0;
    right: 0;
    top: 238px;
    text-align: center;
    font-size: 10.5px;
    font-weight: 400;
    line-height: 1.45;
    color: var(--ink);
  }

  /* Back */
  .company {
    position: absolute;
    left: 44px;
    top: 40px;
    font-size: 24px;
    font-weight: 600;
    line-height: 1.05;
    color: var(--ink);
  }
  .card--back .brand-mark {
    position: absolute;
    right: 40px;
    top: 44px;
    font-size: 28px;
    gap: 10px;
  }
  .card--back .brand-mark__ring { width: 40px; height: 40px; border-width: 5px; }
  .person {
    position: absolute;
    left: 44px;
    top: 166px;
    right: 40px;
  }
  .person__name {
    font-size: 30px;
    font-weight: 700;
    line-height: 1.1;
    color: var(--brand-blue);
  }
  .person__title {
    margin-top: 4px;
    font-size: 13px;
    font-weight: 500;
    color: var(--ink);
    white-space: nowrap;
  }
  .contact {
    position: absolute;
    left: 44px;
    bottom: 34px;
    list-style: none;
    font-size: 15px;
    font-weight: 400;
    line-height: 1.5;
    color: var(--brand-blue);
  }
</style>
</head>
<body>
  <main class="canvas">
    <section class="card card--front" aria-label="Business card, front">
      <div class="brand-mark">
        <span class="brand-mark__ring" aria-hidden="true"></span>
        <span class="brand-mark__name">Tarvik Works</span>
      </div>
      <p class="motto">“We will solve your EMC problems as early as<br>possible—ideally before they even start.”</p>
    </section>

    <section class="card card--back" aria-label="Business card, back">
      <h1 class="company">Tarvik<br>Works, Inc.</h1>
      <div class="brand-mark">
        <span class="brand-mark__ring" aria-hidden="true"></span>
        <span class="brand-mark__name">Tarvik Works</span>
      </div>
      <div class="person">
        <p class="person__name">Dana Whitlock</p>
        <p class="person__title">President and Chief EMC Engineer</p>
      </div>
      <ul class="contact">
        <li class="contact__web">www.tarvikworks.com</li>
        <li class="contact__email">dana@tarvikworks.com</li>
      </ul>
    </section>
  </main>
</body>
</html>
```